Home Page Design (+50 More Pages To Winning Designer!)

We have a 50+ page website, but we're starting with the home page. The winning designer will get all 50+ pages to design as a 2nd project, so make sure you do your best!

SoarVane is in the private jet industry and needs a re-designed website.

We have created the structure for the website and content inside of Tavoni.io (THESE ARE ONLY ROUGH A.I. GENERATED WIREFRAMES AND DO NOT NEED TO BE FOLLOWED EXACTLY) - https://www.tavoni.io/app/project/P482915_qRuVwKsLm-DDtaHrYuop72XNc8fkoPzqlrhwDxHkaWm3Tq

Take the content from the 'Home Page' under the 'Wireframe' tab on the Tavoni.io link above, but feel free to re-design the page in a better way as these are only A.I. generated wireframes.

We want a DARK theme.... High quality, luxurious feel, greyscale colors. Attached is a brand guideline (BUT THIS IS NOT A 100% BRAND GUIDELINE, YOU CAN CHANGE COLORS AND FONTS AND MAKE CHANGES IF YOU HAVE BETTER IDEAS) and attached is our logo. We are also attaching some examples of other apps and websites to give you a guideline of what we're looking for for this design project.

The final design MUST communicate luxury using high-quality imagery of large cabin luxurious private jets.

ENTRIES THAT DO NOT FOLLOW THE PROJECT BRIEF WILL BE AUTOMATICALLY DISCARDED. FOLLOW THE INSTRUCTIONS!

Industry/Entity Type

Travel

Number of Pages Required

1 page

Font styles to use
Sans Serif

Colors

Designer to choose colors to be used in the design.

Requirements
Must have
• Follow wireframe and use content in wireframe (see Tavoni.io link)

```html
<!DOCTYPE html>
<html lang="en">
<head>
<meta charset="utf-8">
<title>SoarVane — Home</title>
<link href="https://fonts.googleapis.com/css2?family=Young+Serif&family=Inter:wght@400;500;600;700&display=swap" rel="stylesheet">
<style>
:root{
  --stage:#262626;
  --ink:#1f1f1f;
  --ink-2:#242424;
  --ink-3:#2c2c2c;
  --copper:#c98a55;
  --copper-soft:#d9a274;
  --paper:#f3f3f3;
  --paper-ink:#2a2a2a;
  --muted:#9a9a9a;
  --line:#3a3a3a;
  --white:#ffffff;
  --olive:#5c5544;
}
*{box-sizing:border-box;margin:0;padding:0}
html,body{width:1200px;height:4167px;overflow:hidden}
body{background:var(--stage);font-family:"Inter",sans-serif;color:var(--white)}
.page{position:absolute;left:217px;top:204px;width:765px}
section,header,footer{position:relative;width:765px;overflow:hidden}
.abs{position:absolute}
.serif{font-family:"Young Serif",serif;font-weight:400}
.accent{color:var(--copper)}
.label{font-size:6px;font-weight:700;letter-spacing:.4px;text-transform:uppercase}
.body-text{font-size:6.5px;line-height:10.5px;color:#c9c9c9}
.dark-text{color:#555}
.btn{position:absolute;height:17px;border-radius:9px;font-size:6px;font-weight:600;display:flex;align-items:center;justify-content:center;text-transform:uppercase;letter-spacing:.3px}
.btn-fill{background:var(--copper);color:var(--white)}
.btn-line{border:1px solid #cfcfcf;color:var(--white)}
.btn-line-dark{border:1px solid #888;color:#333}
.photo{position:absolute}
.icon-dot{display:inline-flex;width:13px;height:13px;border-radius:50%;background:var(--copper);align-items:center;justify-content:center;vertical-align:middle}

/* hero */
.hero{height:373px;background:radial-gradient(ellipse at 65% 40%,#8a7358 0%,#5f4c39 45%,#3f3429 100%)}
.nav-logo{left:110px;top:16px;font-size:15px;display:flex;align-items:center;gap:4px}
.nav-logo .mark{width:9px;height:9px;background:var(--white)}
.nav-links{left:243px;top:21px;display:flex;gap:16px;font-size:6.5px;color:#eee}
.hero h1{left:110px;top:100px;font-size:29px;line-height:32px;width:320px}
.hero .body-text{left:110px;top:208px;width:280px}

/* fractional */
.fractional{height:325px;background:var(--ink)}
.fractional h2{left:386px;top:64px;font-size:21px;line-height:26px;width:300px}
.fractional .body-text{left:386px;top:147px;width:240px}
.feat{font-size:5.8px;display:flex;align-items:center;gap:5px;color:#ddd}

/* options */
.options{height:335px;background:var(--ink-2)}
.opt{left:110px;width:210px}
.opt h3{font-size:14px;line-height:17px;margin-bottom:7px}

/* light cta */
.light{background:var(--paper);color:var(--paper-ink)}
.cta1{height:259px}
.cta1 h2{left:110px;top:58px;font-size:22px;line-height:26px;width:300px}

/* unparalleled */
.unpar{height:344px;background:linear-gradient(180deg,#5d5747 0%,#4c4739 100%)}
.center{left:0;width:765px;text-align:center}
.card{top:157px;width:267px;height:77px;background:rgba(255,255,255,.1);border:1px solid rgba(255,255,255,.15);border-radius:6px;padding:14px 16px}
.card h4{font-size:13px;display:flex;align-items:center;gap:6px;margin-bottom:6px}

/* services */
.services{height:450px;background:var(--ink)}
.svc{width:180px;text-align:center}
.svc h4{font-size:10px;margin:8px 0 4px}
.svc p{font-size:5.5px;line-height:9px;color:#aaa}

/* cta2 */
.cta2{height:202px}
.cta2 h2{left:110px;top:50px;font-size:22px;line-height:26px}

/* testimonials */
.testi{height:354px;background:var(--ink-2)}
.arrow{top:50px;width:46px;height:20px;border-radius:10px;display:flex;align-items:center;justify-content:center}
.quote{width:170px;top:103px}
.stars{font-size:8px;letter-spacing:1px;color:#eee}
.quote h5{font-size:9px;line-height:12px;margin:6px 0 6px;font-family:"Young Serif",serif;font-weight:400}
.quote p{font-size:5.5px;line-height:9px;color:#aaa}
.person{display:flex;gap:6px;align-items:center;margin-top:10px;font-size:5.5px}
.person .av{width:20px;height:20px;border-radius:50%;background:linear-gradient(135deg,#777,#444)}
.person small{display:block;color:#888;font-size:5px}
.partners{top:292px;left:140px;width:485px;display:flex;justify-content:space-between;align-items:center}
.partners span{display:block;background:#d8d8d8;height:10px;border-radius:2px}

/* newsletter */
.news{height:293px}
.news h2{left:110px;top:86px;font-size:22px;line-height:26px}
.field{left:110px;top:184px;width:236px;height:20px;background:var(--white);border-radius:10px;box-shadow:0 1px 4px rgba(0,0,0,.08)}

/* faq */
.faq{height:475px;background:var(--ink)}
.q{left:110px;width:545px;font-size:7.5px;font-family:"Young Serif",serif;display:flex;justify-content:space-between;align-items:center}
.q .toggle{width:13px;height:13px;border-radius:50%;background:#3a3a3a;display:flex;align-items:center;justify-content:center;font-family:"Inter",sans-serif;font-size:8px;color:#ddd}
.rule{left:110px;width:545px;height:1px;background:var(--line)}

/* footer */
.foot{height:399px;background:var(--ink-2)}
.fcol{top:123px;font-size:5.5px;line-height:9.5px;color:#aaa}
.fcol h6{font-size:6.5px;color:var(--white);font-weight:600;margin-bottom:4px;text-decoration:underline}
.social{display:flex;gap:8px}
.social span{width:11px;height:11px;border-radius:50%;background:#555}
</style>
</head>
<body>
<main class="page">

  <!-- HERO -->
  <header class="hero">
    <div class="abs nav-logo serif">SoarVane<span class="mark"></span></div>
    <nav class="abs nav-links"><span>Home</span><span>Aircraft</span><span>Program</span><span>Why SoarVane</span><span>Lifestyle</span></nav>
    <div class="btn btn-line" style="left:514px;top:14px;width:58px">Sign Up</div>
    <div class="btn btn-fill" style="left:583px;top:14px;width:73px">Contact Us</div>
    <h1 class="abs serif">Experience the Ultimate in <span class="accent">Luxury Jet Travel</span></h1>
    <p class="abs body-text">SoarVane offers fractional jet ownership, jet card programs, private jet lease programs, all-access programs, helicopter access programs, and by the seat charter flights. Discover the perfect flight program for your needs.</p>
    <div class="btn btn-fill" style="left:110px;top:262px;width:68px">Explore</div>
    <div class="btn btn-line" style="left:186px;top:262px;width:80px">Learn More</div>
    <div class="photo" role="img" aria-label="White private jet climbing in flight" style="left:318px;top:110px;width:430px;height:175px;background:radial-gradient(ellipse at 50% 50%,rgba(255,255,255,.55) 0%,rgba(255,255,255,.15) 40%,rgba(255,255,255,0) 70%)"></div>
  </header>

  <!-- FRACTIONAL OWNERSHIP -->
  <section class="fractional">
    <div class="photo" role="img" aria-label="Private jet parked with its airstair door open" style="left:0;top:80px;width:340px;height:195px;background:radial-gradient(ellipse at 40% 50%,#e8e8e8 0%,#9a9a9a 38%,rgba(31,31,31,0) 70%)"></div>
    <div class="abs label" style="left:386px;top:46px">Discover</div>
    <h2 class="abs serif">Experience the Luxury of <span class="accent">Fractional Jet Ownership</span></h2>
    <p class="abs body-text">With SoarVane's fractional jet ownership program, you can enjoy the benefits of private jet travel without the hassle and expense of owning a whole aircraft. Our program offers flexibility, convenience, and access to a fleet of luxurious jets, allowing you to travel in style and comfort.</p>
    <div class="abs feat" style="left:386px;top:205px"><span class="icon-dot"></span>Flexible Ownership Options</div>
    <div class="abs feat" style="left:487px;top:205px"><span class="icon-dot"></span>Convenient Booking Process</div>
    <div class="abs feat" style="left:386px;top:228px"><span class="icon-dot"></span>Luxurious Fleet of Jets</div>
    <div class="btn btn-fill" style="left:386px;top:262px;width:80px">Learn More</div>
    <div class="btn btn-line" style="left:474px;top:262px;width:66px">Sign Up</div>
  </section>

  <!-- OPTIONS -->
  <section class="options">
    <div class="abs opt" style="top:50px"><h3 class="serif">Flexible Ownership Options Available</h3><p class="body-text">Choose from a variety of ownership programs and enjoy the freedom to fly on your own terms.</p></div>
    <div class="abs opt" style="top:143px"><h3 class="serif">Convenient Jet Card Programs</h3><p class="body-text">Access a fleet of private jets with our exclusive jet card programs, offering flexibility and convenience.</p></div>
    <div class="abs opt" style="top:240px"><h3 class="serif">Flexible Lease Programs</h3><p class="body-text">Experience the luxury of private jet travel without the commitment with our flexible lease programs.</p></div>
    <div class="photo" role="img" aria-label="Passenger seated in a leather cabin seat aboard a private jet" style="left:383px;top:0;width:382px;height:335px;background:linear-gradient(135deg,#cfcfcf 0%,#8e8e8e 45%,#5e5e5e 100%)"></div>
  </section>

  <!-- CTA ONE -->
  <section class="light cta1">
    <div class="photo" role="img" aria-label="Private jet flying above grey clouds" style="left:330px;top:0;width:435px;height:259px;background:linear-gradient(90deg,var(--paper) 0%,#dcdcdc 60%,#cacaca 100%)"></div>
    <h2 class="abs serif"><span class="accent">Experience the Luxury Travel</span> Like Never Before</h2>
    <p class="abs body-text dark-text" style="left:110px;top:117px;width:275px">Discover the ultimate in private jet travel with SoarVane. Whether you're looking for fractional jet ownership, jet card programs, private jet lease programs, all access programs, helicopter access programs, or by the seat charter flights, we have the perfect solution for your travel needs.</p>
    <div class="btn btn-fill" style="left:110px;top:183px;width:74px">Book Now</div>
    <div class="btn btn-line-dark" style="left:193px;top:183px;width:78px">Contact Us</div>
  </section>

  <!-- UNPARALLELED -->
  <section class="unpar">
    <div class="abs label center" style="top:47px">Experience</div>
    <h2 class="abs serif center" style="top:62px;font-size:21px;line-height:26px"><span class="accent">Unparalleled Luxury and Convenience</span><br>for Private Aviation</h2>
    <p class="abs body-text center" style="top:119px;padding:0 130px;color:#ddd">Discover the ultimate in luxury and convenience with SoarVane. Our exclusive private aviation solutions provide you with unparalleled access to the world of private jets, ensuring a seamless and extraordinary travel experience.</p>
    <div class="abs card" style="left:110px"><h4 class="serif"><span class="icon-dot"></span>Convenience</h4><p class="body-text">Enjoy hassle-free travel with our flexible scheduling and personalized services.</p></div>
    <div class="abs card" style="left:388px"><h4 class="serif"><span class="icon-dot"></span>Luxury</h4><p class="body-text">Indulge in the lavish amenities and exquisite interiors of our private jets.</p></div>
    <div class="btn btn-fill" style="left:342px;top:252px;width:81px">Learn More</div>
    <div class="btn btn-line" style="left:350px;top:280px;width:65px">Sign Up</div>
  </section>

  <!-- SERVICES -->
  <section class="services">
    <div class="abs label center" style="top:47px">Luxury</div>
    <h2 class="abs serif center" style="top:63px;font-size:21px">Experience the <span class="accent">Ultimate in Private Jet</span> Travel</h2>
    <p class="abs body-text center" style="top:93px;padding:0 125px">SoarVane offers a wide range of exclusive services to meet your private jet travel needs. From fractional jet ownership to on-demand charter flights, we provide the highest level of luxury and convenience.</p>
    <div class="abs svc" style="left:292px;top:135px"><span class="icon-dot"></span><h4 class="serif">Global Medical Response &amp; Recovery</h4><p>We provide specialized medical transportation services worldwide.</p></div>
    <div class="abs svc" style="left:127px;top:209px"><span class="icon-dot"></span><h4 class="serif">Fractional Jet Ownership</h4><p>Enjoy the benefits of owning a private jet without the hassles.</p></div>
    <div class="abs svc" style="left:458px;top:209px"><span class="icon-dot"></span><h4 class="serif">On Demand Charter</h4><p>Fly anywhere, anytime with our on-demand charter service.</p></div>
    <div class="photo" role="img" aria-label="Front view of a private jet on the runway" style="left:118px;top:205px;width:530px;height:135px;background:radial-gradient(ellipse at 50% 75%,rgba(255,255,255,.5) 0%,rgba(255,255,255,.12) 35%,rgba(31,31,31,0) 65%)"></div>
    <div class="btn btn-fill" style="left:342px;top:355px;width:81px">Learn More</div>
    <div class="btn btn-line" style="left:350px;top:382px;width:65px">Sign Up</div>
  </section>

  <!-- CTA TWO -->
  <section class="light cta2">
    <div class="photo" role="img" aria-label="Traveller with luggage walking beside a private jet on the apron" style="left:450px;top:0;width:315px;height:202px;background:linear-gradient(90deg,#cfcfcf 0%,#a7a7a7 60%,#8a8a8a 100%)"></div>
    <svg class="abs" style="left:410px;top:0" width="80" height="202" viewBox="0 0 80 202"><path d="M8 0 C60 40 60 160 8 202" fill="none" stroke="#c98a55" stroke-width="4"/><path d="M0 0 C52 40 52 160 0 202 L0 0Z" fill="#f3f3f3"/></svg>
    <h2 class="abs serif">Experience <span class="accent">Luxury<br>Travel</span> Like Never Before</h2>
    <p class="abs body-text dark-text" style="left:110px;top:108px;font-size:8px">Contact us today to book your exclusive jet experience.</p>
    <div class="btn btn-fill" style="left:110px;top:136px;width:80px">Contact Us</div>
  </section>

  <!-- TESTIMONIALS -->
  <section class="testi">
    <div class="abs label" style="left:110px;top:47px">Testimonials</div>
    <h2 class="abs serif" style="left:110px;top:62px;font-size:20px">What People <span class="accent">Say About Us</span> ?</h2>
    <div class="abs arrow" style="left:544px;border:1px solid #bbb"><svg width="9" height="6" viewBox="0 0 9 6"><path d="M9 3H1M3 0.5 0.5 3 3 5.5" stroke="#fff" fill="none"/></svg></div>
    <div class="abs arrow" style="left:606px;background:var(--copper)"><svg width="9" height="6" viewBox="0 0 9 6"><path d="M0 3H8M6 0.5 8.5 3 6 5.5" stroke="#fff" fill="none"/></svg></div>
    <div class="abs quote" style="left:110px"><div class="stars">★★★★★</div><h5>SoarVane's services have exceeded my expectation</h5><p>Every flight was smooth and punctual. The crew was attentive and the cabin felt like a private lounge in the sky.</p><div class="person"><span class="av"></span><div>Mara Ellison<small>Harbor Crest Ltd</small></div></div></div>
    <div class="abs quote" style="left:296px"><div class="stars">★★★★☆</div><h5>SoarVane's services have exceeded my expectation</h5><p>Booking took minutes and the team handled every detail. I now fly with them for all my business travel.</p><div class="person"><span class="av"></span><div>Dorian Vale<small>Maison Rell</small></div></div></div>
    <div class="abs quote" style="left:480px"><div class="stars">★★★★★</div><h5>SoarVane's services have exceeded my expectation</h5><p>Flexible, discreet and truly luxurious. The jet card program fits my schedule perfectly every time.</p><div class="person"><span class="av"></span><div>Theo Marsh<small>Kestrel Works</small></div></div></div>
    <div class="abs rule" style="top:241px"></div>
    <div class="abs serif center" style="top:258px;font-size:11px">Trusted by top-tier companies around the globe</div>
    <div class="abs partners">
      <span style="width:62px"></span><span style="width:36px"></span><span style="width:74px"></span><span style="width:58px"></span><span style="width:66px"></span><span style="width:74px"></span>
    </div>
  </section>

  <!-- NEWSLETTER -->
  <section class="light news">
    <div class="photo" role="img" aria-label="Traveller with a suitcase in front of a private jet" style="left:330px;top:0;width:435px;height:293px;background:linear-gradient(90deg,var(--paper) 0%,#d4d4d4 45%,#b5b5b5 100%)"></div>
    <h2 class="abs serif">Stay <span class="accent">Up To Date</span><br>With Our Newsletter</h2>
    <p class="abs body-text dark-text" style="left:110px;top:147px;width:235px">Receive news on new routes, fleet additions and exclusive member offers straight to your inbox each month.</p>
    <div class="abs field"></div>
    <div class="abs" style="left:120px;top:191px;font-size:5.5px;color:#999">Your email</div>
    <div class="btn btn-fill" style="left:265px;top:186px;width:80px">Subscribe</div>
  </section>

  <!-- FAQ -->
  <section class="faq">
    <div class="abs label center" style="top:52px">FAQ's</div>
    <h2 class="abs serif center" style="top:66px;font-size:21px">Frequently <span class="accent">Ask Question</span></h2>
    <p class="abs body-text center" style="top:97px">Find answer to common question about SoarVane's services and program.</p>
    <div class="abs q" style="top:121px"><span>■ &nbsp;What is SoarVane?</span><span class="toggle">−</span></div>
    <p class="abs body-text" style="left:110px;top:140px;width:530px;font-size:5.8px;line-height:9.5px">SoarVane is a company that offers fractional jet ownership, jet card programs, private jet lease programs, all access programs, helicopter access programs, and by the seat charter flights. We provide flexible and convenient options for individuals and businesses to access private aviation services.</p>
    <div class="abs rule" style="top:172px"></div>
    <div class="abs q" style="top:189px"><span>■ &nbsp;How it works?</span><span class="toggle">+</span></div>
    <div class="abs rule" style="top:214px"></div>
    <div class="abs q" style="top:231px"><span>■ &nbsp;Why choose SoarVane?</span><span class="toggle">+</span></div>
    <div class="abs rule" style="top:256px"></div>
    <div class="abs q" style="top:273px"><span>■ &nbsp;How to book?</span><span class="toggle">+</span></div>
    <div class="abs rule" style="top:298px"></div>
    <div class="abs q" style="top:315px"><span>■ &nbsp;What are the benefits?</span><span class="toggle">+</span></div>
    <div class="abs serif center" style="top:358px;font-size:12px">Still Have Question?</div>
    <p class="abs body-text center" style="top:382px">Contact us for more information.</p>
    <div class="btn btn-fill" style="left:342px;top:410px;width:81px">Contact Us</div>
  </section>

  <!-- FOOTER -->
  <footer class="foot">
    <div class="abs center serif" style="top:50px;font-size:20px;display:flex;justify-content:center;align-items:center;gap:5px">SoarVane<span style="width:12px;height:12px;background:#fff;display:inline-block"></span></div>
    <p class="abs body-text center" style="top:84px;padding:0 105px;font-size:5.8px;line-height:9.5px">SoarVane offers fractional jet ownership, jet card programs, private jet lease programs, all access programs, helicopter access programs, and by the seat charter flights. Discover the perfect flight program for your needs.</p>
    <div class="abs fcol" style="left:110px"><h6>ABOUT US</h6>Charter<br>Fleet<br>Destinations<br>Pricing<br>Contact</div>
    <div class="abs fcol" style="left:241px"><h6>SERVICE</h6>Private Jet<br>Helicopters<br>Jet Cards<br>Membership<br>FAQ</div>
    <div class="abs fcol" style="left:369px"><h6>TERMS</h6>Privacy<br>Careers<br>Press<br>Blog<br>Support</div>
    <div class="abs fcol" style="left:496px;top:130px;width:160px"><h6 style="text-decoration:none">SUBSCRIBE OUR NEWSLETTER</h6>Join our mailing list for the latest updates<div style="margin-top:5px;height:17px;background:#333;border-radius:9px;padding-left:10px;line-height:17px;font-size:5px">your email</div><div style="font-size:4.5px;line-height:7px;margin-top:4px;color:#777">By subscribing you agree to our Privacy Policy and consent to receive updates.</div></div>
    <div class="btn btn-fill" style="left:594px;top:167px;width:58px;height:15px">Subscribe</div>
    <div class="abs rule" style="top:232px"></div>
    <div class="abs" style="left:114px;top:243px;font-size:5.8px;color:#aaa;display:flex;gap:14px"><span>© 2023 SoarVane. All rights reserved.</span><u>Privacy Policy</u><u>Terms of Service</u><u>Cookie Settings</u></div>
    <div class="abs social" style="left:580px;top:241px"><span></span><span></span><span></span><span></span><span></span></div>
    <div class="photo" role="img" aria-label="Dark silhouette of a private jet on the tarmac" style="left:0;top:265px;width:765px;height:134px;background:radial-gradient(ellipse at 50% 70%,#4a4a4a 0%,#2d2d2d 40%,#1c1c1c 80%)"></div>
  </footer>

</main>
</body>
</html>
```